Coffee and Plastics

I am looking for a completely new site that shows the products we have. Our current site is www.velmorebrothersroast.com. We are open minded to what designers come up with. Our current site is www.velmorebrothersroast.com. You can you the information from there to start the site. I need these tabs on the main home page. ( Home, Coffee & Tea, Condiments, and Paper and Plastics, and Contact.) You can take photos and info from my Current site. In products page.
I will be uploading info and photo for paper and plastics.
Look and feel
Each slider illustrates characteristics of the customer's brand and the style your logo design should communicate.

```html
<!DOCTYPE html>
<html lang="en">
<head>
<meta charset="utf-8">
<title>Velmore Brothers Roast</title>
<link href="https://fonts.googleapis.com/css2?family=Marcellus+SC&family=Open+Sans:wght@400;600&family=Oswald:wght@500;700&family=Signika:wght@600&family=Montserrat:wght@500&display=swap" rel="stylesheet">
<style>
:root{
  --brown:#3a2410;
  --brown-dark:#24160a;
  --red:#e8321f;
  --ink:#2b2b2b;
  --muted:#777;
  --line:#cfcfcf;
  --topbar:#f2f2f2;
  --footer-bg:#f7f7f7;
  --bottom:#121212;
  --hero-a:#d6edf0;
  --hero-b:#eef8f9;
  --tile:#1e1e1e;
}
*{box-sizing:border-box;margin:0;padding:0}
html,body{width:822px;height:1200px;overflow:hidden;background:#fff}
body{position:relative;font-family:"Open Sans",sans-serif;color:var(--ink)}
.abs{position:absolute}
.topbar{left:0;top:0;width:822px;height:32px;background:var(--topbar)}
.select{top:8px;height:18px;background:#fff;border:1px solid #e2e2e2;font-size:8px;padding:4px 6px;display:flex;justify-content:space-between;align-items:center}
.toplinks{right:88px;top:11px;display:flex;font-size:7.5px;color:#444}
.toplinks span{padding:0 13px;border-left:1px solid #ccc}
.toplinks span:first-child{border:none}
.logo{left:82px;top:56px;font-family:"Marcellus SC",serif;font-size:18px;letter-spacing:.3px;color:#1c1c1c}
.cart{left:600px;top:54px;width:130px;height:25px;border:1px solid #ddd;display:flex;align-items:center;font-size:8px;color:#444;padding-left:8px}
.cart b{color:var(--brown);font-weight:600}
.cart-btn{position:absolute;right:-1px;top:-1px;width:26px;height:25px;background:var(--brown);display:flex;align-items:center;justify-content:center}
.nav{left:0;top:100px;width:822px;height:34px;background:var(--brown)}
.nav ul{list-style:none;position:absolute;left:82px;top:0;display:flex;height:34px}
.nav li{color:#fff;font-size:10px;letter-spacing:.4px;padding:0 15px;line-height:34px}
.nav li.active{background:var(--brown-dark)}
.search{left:595px;top:108px;width:115px;height:19px;background:#fff;font-size:6.5px;color:#555;padding:6px 7px}
.search-btn{left:710px;top:108px;width:22px;height:19px;background:#fff;border-left:1px solid #ccc;display:flex;align-items:center;justify-content:center}
.hero{left:0;top:134px;width:822px;height:256px;background:linear-gradient(180deg,var(--hero-a),var(--hero-b))}
.hero h1{position:absolute;left:82px;top:62px;font-family:"Marcellus SC",serif;font-weight:400;color:#1c1c1c;line-height:1}
.hero h1 .small{display:block;font-size:18px}
.hero h1 .big{display:block;font-size:23px;margin-top:5px}
.hero p{position:absolute;left:82px;top:120px;width:295px;font-size:9.3px;line-height:14px;color:#333}
.btn-more{position:absolute;left:82px;top:178px;width:108px;height:21px;background:var(--brown-dark);color:#fff;font-family:"Montserrat",sans-serif;font-size:10px;display:flex;align-items:center;justify-content:center}
.hero-photo{position:absolute;left:400px;top:10px;width:340px;height:230px;background:radial-gradient(ellipse at 62% 50%,rgba(248,248,246,.95) 0%,rgba(205,185,165,.55) 45%,rgba(214,237,240,0) 72%)}
.dots{left:386px;top:370px;width:52px;height:19px;background:var(--brown-dark);display:flex;align-items:center;justify-content:center;gap:3px}
.dots i{width:8px;height:8px;border-radius:50%;background:#fff}
.dots i.on{background:var(--red)}
.feature{top:437px;width:158px;height:205px;border:1px solid #666}
.feature .ph{position:absolute;left:9px;top:7px;width:138px;height:121px;background:radial-gradient(ellipse at center,#9a9a9a 0 30%,#3a3a3a 55%,var(--tile) 75%)}
.feature .t{position:absolute;left:9px;top:138px;font-family:"Signika",sans-serif;font-size:23px;color:var(--red);letter-spacing:.5px}
.feature .s{position:absolute;left:10px;top:170px;font-family:"Oswald",sans-serif;font-weight:700;font-size:15px;color:#222}
.newbar{left:86px;top:670px;width:651px;height:21px;border-top:1px solid var(--line);border-bottom:1px solid var(--line)}
.newbar span{position:absolute;left:6px;top:4px;font-family:"Oswald",sans-serif;font-weight:700;font-size:10px;color:var(--red)}
.newbar svg{position:absolute;right:6px;top:5px}
.product{top:700px;width:153px;height:167px;border:1px solid #ddd}
.product .ph{position:absolute;left:6px;top:5px;width:139px;height:121px;background:radial-gradient(ellipse at center,#8a8a8a 0 22%,#444 55%,#2c2c2c 80%)}
.product .actions{position:absolute;left:0;right:0;top:139px;display:flex;justify-content:center;gap:5px}
.add{width:52px;height:19px;background:#4a2415;color:#fff;font-size:7px;display:flex;align-items:center;justify-content:center}
.view{width:34px;height:19px;background:#f1f1f1;border:1px solid #ddd;color:#555;font-size:7px;display:flex;align-items:center;justify-content:center}
.foot{left:0;top:896px;width:822px;height:268px;background:var(--footer-bg);border-top:1px solid #e8e8e8}
.col-title{top:930px;font-size:17.5px;font-weight:400;color:#333}
.col-title b{font-weight:600}
.blog-h{left:82px;top:969px;font-size:12px;font-weight:600;color:#333}
.blog-d{left:82px;top:988px;font-size:8.5px;color:var(--muted)}
.blog-p{left:82px;top:1009px;width:200px;font-size:8.5px;line-height:16px;color:#444}
.full{left:82px;top:1098px;font-size:8.5px;color:var(--red)}
.tweets{left:322px;top:972px;width:187px;height:150px;background:#fff;border:1px solid #ddd}
.tweet{padding:12px 12px 0;font-size:8px;line-height:13.5px;color:#444;height:68px}
.tweet+.tweet{border-top:1px solid #ddd;height:81px}
.tweet a{color:var(--red);text-decoration:none}
.tweet small{display:block;margin-top:5px;font-size:7px;color:var(--muted)}
.stay-p{left:562px;top:964px;width:185px;font-size:8.5px;line-height:15px;color:#444}
.contact{left:562px;font-size:8px;color:#444;display:flex;align-items:center;gap:9px}
.rule{left:562px;top:1069px;width:149px;height:1px;background:#ddd}
.social{top:1081px;width:10px;height:10px;background:#666;border-radius:2px}
.bottom{left:0;top:1164px;width:822px;height:36px;background:var(--bottom)}
.copy{left:82px;top:1178px;font-size:9px;color:#ddd}
.pay{top:1175px;width:22px;height:14px;border-radius:2px}
</style>
</head>
<body>
<div class="abs topbar"></div>
<div class="abs select" style="left:82px;width:60px"><span>English</span><svg width="6" height="4"><path d="M0 0h6L3 4z" fill="#333"/></svg></div>
<div class="abs select" style="left:151px;width:52px"><span>USD</span><svg width="6" height="4"><path d="M0 0h6L3 4z" fill="#333"/></svg></div>
<div class="abs toplinks"><span>My Account</span><span>My Wishlist</span><span>My Cart</span><span>Checkout</span><span>Log In</span></div>

<div class="abs logo">Velmore Brothers Roast</div>
<div class="abs cart">Shopping cart - <b>&nbsp;$0.00</b>
  <div class="cart-btn"><svg width="13" height="11" viewBox="0 0 13 11"><path d="M0 1h2.5l1.8 6h6.5l1.6-4.5H3.4" fill="none" stroke="#fff" stroke-width="1.4"/><circle cx="5" cy="9.5" r="1.1" fill="#fff"/><circle cx="10" cy="9.5" r="1.1" fill="#fff"/></svg></div>
</div>

<nav class="abs nav"><ul><li class="active">HOME</li><li>COFFEE &amp; TEA</li><li>CONDIMENTS</li><li>PAPER AND PLASTICS</li><li>CONTACT</li></ul></nav>
<div class="abs search">SEARCH HERE</div>
<div class="abs search-btn"><svg width="9" height="9" viewBox="0 0 9 9"><circle cx="3.7" cy="3.7" r="2.8" fill="none" stroke="#222" stroke-width="1.3"/><path d="M5.8 5.8L8.5 8.5" stroke="#222" stroke-width="1.4"/></svg></div>

<section class="abs hero">
  <h1><span class="small">Welcome to the</span><span class="big">Velmore Brothers Roast</span></h1>
  <p>Lorem ipsum dolor sit amet elit, sed dout labore et dolore magna aliqua. Ut enim ad minim veniam quis nostrud &nbsp;ullamco laboris nisi ut aliquip ex ea commodo consequat.</p>
  <div class="btn-more">Read More</div>
  <div class="hero-photo" role="img" aria-label="Photo of a cup of black coffee on a saucer with scattered roasted coffee beans"></div>
</section>
<div class="abs dots"><i></i><i></i><i class="on"></i><i></i></div>

<div class="abs feature" style="left:86px"><div class="ph" role="img" aria-label="Clear plastic compartment tray"></div><div class="t">Sitw kia</div><div class="s">COFFEE</div></div>
<div class="abs feature" style="left:250px"><div class="ph" role="img" aria-label="Round clear plastic platter with lid"></div><div class="t">Sitw kia</div><div class="s">COFFEE</div></div>
<div class="abs feature" style="left:414px"><div class="ph" role="img" aria-label="White plastic meal tray"></div><div class="t">Lipsum</div><div class="s">COFFE</div></div>
<div class="abs feature" style="left:579px"><div class="ph" role="img" aria-label="White plastic compartment plate"></div><div class="t">SITQUET</div><div class="s">COFFEE</div></div>

<div class="abs newbar"><span>NEW PRODUCTS</span><svg width="18" height="9" viewBox="0 0 18 9"><path d="M6 0v9L0 4.5z" fill="#222"/><path d="M12 0v9l6-4.5z" fill="#222"/></svg></div>

<div class="abs product" style="left:86px"><div class="ph" role="img" aria-label="White plastic cutlery set"></div><div class="actions"><div class="add">Add To Cart</div><div class="view">View</div></div></div>
<div class="abs product" style="left:252px"><div class="ph" role="img" aria-label="Round divided plastic plate"></div><div class="actions"><div class="add">Add To Cart</div><div class="view">View</div></div></div>
<div class="abs product" style="left:418px"><div class="ph" role="img" aria-label="Paper coffee cup with white lid"></div><div class="actions"><div class="add">Add To Cart</div><div class="view"></div></div></div>
<div class="abs product" style="left:584px"><div class="ph" role="img" aria-label="Gold plastic fork and spoon"></div><div class="actions"><div class="add">Add To Cart</div><div class="view">View</div></div></div>

<div class="abs foot"></div>
<h2 class="abs col-title" style="left:82px">From <b>Our Blog</b></h2>
<h2 class="abs col-title" style="left:322px">Recent <b>Tweets</b></h2>
<h2 class="abs col-title" style="left:562px">Stay <b>in Touch</b></h2>

<div class="abs blog-h">Lorem ipsum dolor sit amet</div>
<div class="abs blog-d">14<sup style="font-size:5px">th</sup> November</div>
<p class="abs blog-p">Nam libero tempore, cum soluta nobis est eligendi optio cumque nihil impedit quo lorem ipsum dolor sit &nbsp;minus id quod maxime placeat facere possimus, omnis voluptas assumenda est, omnis dolor repellendus...</p>
<div class="abs full">FULL ARTICLE &nbsp;›</div>

<div class="abs tweets">
  <div class="tweet"><a>@roastnotes</a> Lorem ipsum dolor sit amet consectetur adipisicing elit.<small>9 hours ago</small></div>
  <div class="tweet"><a>@brewline</a> At vero eos et accusamus et iusto odio dignissimos ducimus blanditiis praesentium voluptatum<small>1 day ago</small></div>
</div>

<p class="abs stay-p">Morbi pellentesque felis id arcu lorem ipsum sollicitudin.</p>
<div class="abs contact" style="top:1010px"><svg width="8" height="10" viewBox="0 0 8 10"><rect x="1" y="0.5" width="6" height="9" rx="1" fill="none" stroke="#333"/><rect x="3" y="7.5" width="2" height="1" fill="#333"/></svg>(+00) 1234 56 789</div>
<div class="abs contact" style="top:1028px"><svg width="10" height="8" viewBox="0 0 10 8"><rect width="10" height="8" fill="#333"/><path d="M0 0l5 4 5-4" fill="none" stroke="#fff"/></svg>support@velmoreroast.com</div>
<div class="abs contact" style="top:1046px"><svg width="8" height="10" viewBox="0 0 8 10"><path d="M4 10C1 6 0 4.5 0 3.5a4 4 0 018 0C8 4.5 7 6 4 10z" fill="#333"/><circle cx="4" cy="3.6" r="1.3" fill="#fff"/></svg>22nd Street, 18 440, Colorado</div>
<div class="abs rule"></div>
<div class="abs social" style="left:564px"></div>
<div class="abs social" style="left:583px"></div>
<div class="abs social" style="left:602px"></div>
<div class="abs social" style="left:621px"></div>

<div class="abs bottom"></div>
<div class="abs copy">© Copyright 2014 by Velmore Brothers Roast. All Rights Reserved.</div>
<div class="abs pay" style="left:614px;background:#d8d8d8"></div>
<div class="abs pay" style="left:641px;background:#eeeeee"></div>
<div class="abs pay" style="left:667px;background:#3b8ed0"></div>
<div class="abs pay" style="left:694px;background:#2a3f9b"></div>
<div class="abs pay" style="left:720px;background:#f2b233"></div>
</body>
</html>
```